Company business card

We need a new business card design. We are IT company which is specialized for outsourcing of operations hardware and software (specially Quorvane, we are a partner), developing custom applications and web applications, BPM solutions, auditing hw and sw. actually design was attached. But we need completely NEW.

Business

```html
<!DOCTYPE html>
<html lang="sk">
<head>
<meta charset="utf-8">
<title>Veldrix – business card</title>
<link rel="stylesheet" href="https://fonts.googleapis.com/css2?family=Jost:wght@500&family=Questrial&display=swap">
<style>
  :root {
    --backdrop: #1c1c1c;
    --paper: #f4f4f4;
    --card-dark: #5b5b5b;
    --brand-blue: #1d5aa6;
    --brand-grey: #5e5e5e;
    --ink: #2b2b2b;
    --rule: #d4d4d4;
    --logo-light: #e2e2e2;
  }
  * { margin: 0; padding: 0; box-sizing: border-box; }
  html, body { width: 1200px; height: 1001px; overflow: hidden; }
  body { background: var(--backdrop); position: relative; font-family: "Questrial", sans-serif; }

  .card { position: absolute; width: 589px; height: 329px; box-shadow: 0 6px 16px rgba(0,0,0,.5); overflow: hidden; }
  .card--front { left: 203px; top: 133px; background: var(--paper); }
  .card--back { left: 408px; top: 539px; background: var(--card-dark); }

  .brand {
    position: absolute;
    font-family: "Jost", sans-serif; font-weight: 500;
    letter-spacing: 4px; line-height: 1; white-space: nowrap;
  }
  .card--front .brand { left: 0; width: 294px; top: 150px; text-align: center; font-size: 30px; color: var(--brand-grey); }
  .card--back .brand { left: 45px; top: 224px; font-size: 36px; color: var(--logo-light); }

  .divider { position: absolute; left: 294px; top: 77px; width: 1px; height: 174px; background: var(--rule); }

  .contact { position: absolute; left: 333px; top: 86px; color: var(--ink); }
  .contact__name { font-family: "Jost", sans-serif; font-weight: 500; font-size: 18px; color: var(--brand-blue); letter-spacing: .3px; line-height: 22px; }
  .contact__role { font-size: 14px; line-height: 16px; }
  .contact__list { list-style: none; margin-top: 18px; font-size: 14px; line-height: 18px; }
  .contact__list li { display: flex; align-items: center; gap: 7px; }
  .contact__list svg { width: 14px; height: 14px; flex: none; }
  .contact__address { margin-top: 16px; font-size: 14px; line-height: 18px; font-style: normal; }

  .band { position: absolute; left: 0; bottom: 0; width: 589px; height: 19px; }
</style>
</head>
<body>
  <section class="card card--front">
    <div class="brand">VELDRIX</div>
    <div class="divider"></div>
    <div class="contact">
      <p class="contact__name">LUKÁŠ BREZINA</p>
      <p class="contact__role">CEO</p>
      <ul class="contact__list">
        <li><svg viewBox="0 0 14 14"><rect width="14" height="14" rx="2" fill="#1d5aa6"/><rect x="4.5" y="2.5" width="5" height="9" rx="1" fill="none" stroke="#fff" stroke-width="1.2"/></svg>+421 (0) 900 555 214</li>
        <li><svg viewBox="0 0 14 14"><rect width="14" height="14" rx="2" fill="#1d5aa6"/><rect x="2.5" y="4" width="9" height="6" fill="none" stroke="#fff" stroke-width="1.1"/><path d="M2.5 4 7 7.5 11.5 4" fill="none" stroke="#fff" stroke-width="1.1"/></svg>lukas.brezina@veldrix.sk</li>
        <li><svg viewBox="0 0 14 14"><rect width="14" height="14" rx="2" fill="#1d5aa6"/><circle cx="7" cy="7" r="4.5" fill="none" stroke="#fff" stroke-width="1"/><ellipse cx="7" cy="7" rx="2" ry="4.5" fill="none" stroke="#fff" stroke-width="1"/><path d="M2.5 7h9" stroke="#fff" stroke-width="1"/></svg>www.veldrix.sk</li>
      </ul>
      <address class="contact__address">Lipová 12<br>811 04 Bratislava</address>
    </div>
    <svg class="band" viewBox="0 0 589 19" preserveAspectRatio="none">
      <polygon points="0,0 285,0 296,19 0,19" fill="#5e5e5e"/>
      <polygon points="296,0 589,0 589,19 285,19" fill="#1d5aa6"/>
    </svg>
  </section>

  <section class="card card--back">
    <div class="brand">VELDRIX</div>
  </section>
</body>
</html>
```